Name card design for KOV mobile accessories company

KOV is an upmarket brand, we are looking for professional business card design.

the design should be neat and simple but giving a strong feeling.
should not be colorful. make it black/white/gray tone

Name:
Job title:
Contact no.:
company address: i would like the company address to be very small and thin.
link to social media profile:
company website:

*the company have no website yet
as the project is done please i also would like the font that use in design as well; for more further people in company need a business card:)
Updates

Thank you for all super fast submission :D they're all look cool!

i have just update my brief to make the statement clearer, please check it out :)
if you have any question please dont hesitate to ask.
i would like see more design from you! 
Keep it up!  :D

Target Market(s)

Company target are upmarket company distributor, such as Vordane and Pilto store.

Industry/Entity Type

Business

Font styles to use
Serif
Sans Serif
Other font styles liked:
• Formal and mordern

Colors
ffffff
eeeeee
d3d3d3
919191
474747
1b1b1b
000000
333333

Requirements
Must have
• The design must be professional clean and clear but also Strong and Modern!
text should be formal and mordern
Should not have
• No complicated design!

```html
<!DOCTYPE html>
<html lang="en">
<head>
<meta charset="utf-8">
<title>KOV Mobile Accessories – Business Card</title>
<link rel="stylesheet" href="https://fonts.googleapis.com/css2?family=Josefin+Sans:wght@300;400;600&display=swap">
<style>
  :root {
    --stage: #e4e4e4;
    --card: #1b1b1b;
    --ink-silver: #d3d3d3;
    --ink-grey: #919191;
    --ink-white: #eeeeee;
    --rule: #474747;
  }
  * { box-sizing: border-box; margin: 0; padding: 0; }
  html, body { width: 1200px; height: 900px; overflow: hidden; }
  body {
    background: var(--stage);
    font-family: "Josefin Sans", sans-serif;
    display: flex;
    flex-direction: column;
    align-items: center;
    justify-content: center;
    gap: 40px;
  }
  .card {
    width: 560px;
    height: 320px;
    background: var(--card);
    position: relative;
  }
  /* Front */
  .card-front {
    display: flex;
    flex-direction: column;
    align-items: center;
    justify-content: center;
    gap: 14px;
  }
  .brand-name {
    font-weight: 400;
    font-size: 96px;
    letter-spacing: 10px;
    line-height: 1;
    color: var(--ink-silver);
    padding-left: 10px;
  }
  .brand-tagline {
    font-weight: 300;
    font-size: 13px;
    letter-spacing: 7px;
    color: var(--ink-grey);
    text-transform: uppercase;
  }
  /* Back */
  .card-back {
    display: grid;
    grid-template-columns: 1fr 1px 1fr;
    padding: 44px 40px;
    column-gap: 24px;
  }
  .company-address {
    font-weight: 300;
    font-size: 11px;
    line-height: 1.7;
    letter-spacing: 1px;
    color: var(--ink-grey);
  }
  .divider { background: var(--rule); height: 150px; }
  .person { display: flex; flex-direction: column; align-items: flex-end; }
  .person-name {
    font-weight: 300;
    font-size: 15px;
    letter-spacing: 1.5px;
    color: var(--ink-grey);
  }
  .person-title {
    font-weight: 600;
    font-size: 13px;
    letter-spacing: 2px;
    color: var(--ink-white);
    margin-top: 6px;
  }
  .contact-list {
    list-style: none;
    margin-top: 46px;
    text-align: right;
    font-weight: 300;
    font-size: 12px;
    line-height: 1.8;
    letter-spacing: 1.5px;
    color: var(--ink-silver);
  }
</style>
</head>
<body>
  <section class="card card-front" aria-label="Card front">
    <div class="brand-name">KOV</div>
    <div class="brand-tagline">Mobile · Accessories</div>
  </section>

  <section class="card card-back" aria-label="Card back">
    <address class="company-address" style="font-style:normal">
      KOV pty. ltd<br>
      12 Harlow lane<br>
      4021 Eastvale<br>
      VIC Aus
    </address>
    <div class="divider"></div>
    <div class="person">
      <div class="person-name">Marten L. Okoye</div>
      <div class="person-title">DIRECTOR</div>
      <ul class="contact-list">
        <li>m. 555 018 274</li>
        <li>p. 5550 1937</li>
        <li>www.kovmobile.co</li>
        <li>mail@kovmobile.co</li>
      </ul>
    </div>
  </section>
</body>
</html>
```